New design for our website – modern, elegant, and customer-focused

We want to redesign our website, www.kalmenstrand.se, to create a completely new look that reflects the high quality of our products and services. We are seeking assistance in developing a modern, clean, and user-friendly web experience in Flatsome that strengthens our brand and makes it easier for customers to find the right solutions. Our goal is to enhance the design, functionality, and overall impression to better meet today’s expectations and demands.

Target Market(s)

swimmingpool & spa

Industry/Entity Type

Poolbusiness

Coding

Coded - Design and coding required

Number of Pages Required

1 page

Font styles to use
Other font styles liked:
• HaboroSoft

Requirements
Must have
• We working in Flatsome
Nice to have
• From dream to reality – swimming pools that transform your garden into a place of life and enjoyment.
Should not have
• Nice look

```html
<!DOCTYPE html>
<html lang="en">
<head>
<meta charset="utf-8">
<title>Kalmen Strand – Pools, Enclosures and Spas</title>
<link rel="stylesheet" href="https://fonts.googleapis.com/css2?family=DM+Serif+Display&family=Poppins:wght@400;500;600;700&display=swap">
<style>
:root{
  --navy:#15294a;
  --navy-deep:#13223a;
  --blue:#1f6fa6;
  --blue-head:#2a86c9;
  --sky:#45b4e6;
  --sky-2:#38a6dc;
  --ink:#3a4654;
  --mist:#eaf4fb;
  --line:#d7e7f3;
  --white:#ffffff;
}
*{box-sizing:border-box;margin:0;padding:0}
html,body{width:1200px;height:1200px;overflow:hidden;background:#fff}
body{font-family:"Poppins",sans-serif;color:var(--ink);position:relative}
.page{position:absolute;left:505px;top:33px;width:1220px;height:7300px;transform:scale(.15528);transform-origin:0 0;background:#fff;overflow:hidden}
section,footer,header{position:absolute;left:0;width:1220px;overflow:hidden}
.abs{position:absolute}
.serif{font-family:"DM Serif Display",serif;font-weight:400}
.h-section{font-family:"DM Serif Display",serif;font-size:40px;line-height:1.15;color:var(--blue-head)}
.body-text{font-size:13px;line-height:1.55;color:var(--ink)}
.btn{position:absolute;height:44px;border-radius:22px;display:flex;align-items:center;justify-content:center;font-size:12px;font-weight:600;letter-spacing:.06em;color:#fff;text-transform:uppercase}
.btn-sky{background:linear-gradient(90deg,#4fc3f0,#2f9ad6)}
.btn-fade{background:linear-gradient(90deg,#5cc6f2,#1f4f8a)}
.btn-navy{background:var(--navy)}
.btn-sm{height:40px;font-size:11px;border-radius:20px}

/* hero */
.hero{top:0;height:676px}
.hero-photo{position:absolute;inset:0;background:linear-gradient(180deg,#0c1a2c 0%,#24364a 35%,#8a6a45 52%,#2a6f9e 62%,#1a5a86 80%,#0f3552 100%)}
.nav{position:absolute;left:40px;top:36px;width:1140px;height:80px;background:#fff;border-radius:40px;display:flex;align-items:center;padding:0 40px}
.brand{font-size:22px;font-weight:500;color:var(--blue)}
.menu{display:flex;gap:16px;margin-left:70px;font-size:11px;font-weight:500;color:var(--navy)}
.tools{margin-left:auto;display:flex;gap:12px}
.hero-title{left:88px;top:220px;font-size:68px;line-height:1.15;color:#fff}
.hero-text{left:88px;top:400px;width:520px;font-size:14px;line-height:1.5;color:#e9f1f8}
.dots{left:110px;top:624px;display:flex;gap:10px}
.dots i{width:8px;height:8px;border-radius:50%;background:rgba(255,255,255,.5)}
.dots i.on{background:#fff}

/* intro */
.intro{top:676px;height:412px}
.intro-title{left:88px;top:112px;width:500px}
.intro-sub{left:88px;top:292px;font-size:15px;font-weight:600;color:var(--navy)}
.divider{left:612px;top:110px;width:1px;height:210px;background:var(--line)}
.intro-text{left:660px;top:116px;width:480px}

/* products */
.products{top:1088px;height:432px}
.center-title{width:100%;text-align:center;color:var(--navy)}
.product{position:absolute;top:132px;width:164px;height:232px;border:2px solid var(--line);border-radius:82px 82px 24px 24px;background:#fff;text-align:center}
.product .thumb{width:140px;height:140px;border-radius:50%;margin:10px auto 8px;background:linear-gradient(180deg,#9cc7e6,#2f86c1)}
.product span{font-size:14px;font-weight:600;color:var(--navy);line-height:1.2;display:block}
.arrow{position:absolute;top:232px;width:36px;height:36px}

/* plan band */
.plan{top:1520px;height:460px;background:linear-gradient(135deg,#1c6ea6,#1a5f92 60%,#2578b0)}
.plan-title{left:88px;top:84px;font-size:40px;line-height:1.15;color:#fff}
.plan-text{left:88px;top:216px;width:480px;font-size:13px;line-height:1.55;color:#e6f1f9}
.checks{left:668px;top:108px;font-size:13px;color:#fff}
.checks li{list-style:none;display:flex;align-items:center;gap:12px;height:52px}

/* create */
.create{top:1980px;height:888px}
.create-sub{top:114px;width:100%;text-align:center;font-size:14px;font-weight:600;color:var(--blue-head)}
.create-text{top:150px;left:140px;width:940px;text-align:center;font-size:13px;line-height:1.5}
.tile{position:absolute;width:436px;height:256px;border-radius:14px;overflow:hidden}
.tile span{position:absolute;left:26px;bottom:18px;font-size:14px;font-weight:600;color:#fff;letter-spacing:.04em}

/* feature rows */
.feature{height:504px}
.block{position:absolute;top:0;height:100%;background:linear-gradient(160deg,#1e6da5,#175888)}
.block-left{left:0;width:340px}
.block-right{left:912px;width:308px;background:linear-gradient(160deg,#2a9ad4,#1a79b6)}
.frame{position:absolute;width:558px;height:340px;border:6px solid #fff;border-radius:14px;box-shadow:0 6px 16px rgba(0,0,0,.15)}
.f-right .frame{left:98px;top:60px}
.f-right .ftext{left:704px}
.f-left .frame{left:560px;top:100px}
.f-left .ftext{left:104px}
.ftext{position:absolute;top:100px;width:420px}
.ftitle{font-size:40px;line-height:1.15;color:var(--blue-head)}
.fsub{margin-top:14px;font-size:14px;font-weight:600;color:var(--navy);line-height:1.45}
.fbody{margin-top:16px;font-size:12px;line-height:1.6;text-align:justify}
.fbtns{position:relative;margin-top:28px;height:40px}
.mini-list{margin-top:14px;font-size:12px;line-height:1.9}
.mini-list b{display:block;color:var(--navy);font-weight:600}
.mini-list span{display:flex;align-items:center;gap:8px}

/* summer */
.summer{top:5460px;height:552px;background:linear-gradient(120deg,#2a8fc9,#3fb0df 45%,#7fd0ee 70%,#3aa7d8)}
.summer-title{left:88px;top:136px;font-size:66px;line-height:1.15;color:#fff}
.summer-text{left:88px;top:300px;width:560px;font-size:13px;line-height:1.55;color:#eef7fc}

/* reviews */
.reviews{top:6012px;height:804px;background:var(--mist)}
.rating{left:88px;top:240px;width:1044px;height:72px;background:#fff;border-radius:10px;display:flex;align-items:center;padding:0 24px;gap:40px;font-size:14px;font-weight:600;color:var(--navy)}
.stars{color:#f5b922;letter-spacing:4px;font-size:22px}
.card{position:absolute;top:340px;width:336px;height:404px;background:#fff;border-radius:10px;padding:26px 24px}
.card h4{font-size:14px;font-weight:600;color:var(--navy)}
.card .stars{font-size:20px;margin:8px 0 14px}
.card p{font-size:12px;line-height:1.6}
.g-mark{position:absolute;right:22px;top:22px;width:16px;height:16px;border-radius:50%;border:2px solid #9aa6b2}

/* footer */
.footer{top:6816px;height:484px;background:var(--navy-deep);color:#c9d4e2}
.f-brand{left:88px;top:76px;font-size:30px;font-weight:500;color:var(--sky)}
.f-contact{left:88px;top:150px;font-size:12px;line-height:2.2}
.socials{left:88px;top:248px;display:flex;gap:10px}
.socials i{width:16px;height:16px;border-radius:3px;background:var(--sky)}
.fcol{position:absolute;top:76px;font-size:11px;line-height:2.1}
.fcol h5{font-size:11px;font-weight:600;color:var(--sky);letter-spacing:.05em}
.bottom-bar{position:absolute;left:0;bottom:0;width:100%;height:68px;background:var(--sky-2);color:#fff;font-size:12px;display:flex;align-items:center;justify-content:center}
</style>
</head>
<body>
<div class="page">

  <header class="hero">
    <div class="hero-photo" role="img" aria-label="Photo of a modern villa at dusk with an illuminated swimming pool"></div>
    <nav class="nav">
      <div class="brand">Kalmen Strand</div>
      <div class="menu"><span>Webshop</span><span>Pools</span><span>Pool roof</span><span>Hot tub</span><span>Pool accessories</span><span>Campaigns</span><span>About us</span><span>Contact</span><span>EN</span></div>
      <div class="tools">
        <svg width="16" height="16" viewBox="0 0 16 16" fill="none" stroke="#15294a" stroke-width="2"><circle cx="7" cy="7" r="5"/><path d="M11 11l4 4"/></svg>
        <svg width="16" height="16" viewBox="0 0 16 16" fill="none" stroke="#15294a" stroke-width="2"><circle cx="8" cy="5" r="3"/><path d="M2 15c1-4 11-4 12 0"/></svg>
        <svg width="16" height="16" viewBox="0 0 16 16" fill="none" stroke="#15294a" stroke-width="2"><path d="M1 2h3l2 9h8l2-6H5"/><circle cx="7" cy="14" r="1"/><circle cx="13" cy="14" r="1"/></svg>
      </div>
    </nav>
    <h1 class="abs hero-title serif">Pools That<br>Bring You Closer</h1>
    <p class="abs hero-text">Lorem ipsum is simply dummy text of the printing and typesetting industry. Lorem ipsum has been the industry's standard dummy text ever since.</p>
    <div class="btn btn-sky" style="left:88px;top:482px;width:320px">Get your free estimate</div>
    <div class="abs dots"><i></i><i></i><i></i><i class="on"></i><i></i></div>
  </header>

  <section class="intro">
    <svg class="abs" style="left:0;top:0" width="1220" height="412" fill="none" stroke="#dbeaf5" stroke-width="2">
      <path d="M0 40 C300 10 600 70 1220 30"/><path d="M0 60 C350 30 700 90 1220 50"/>
      <path d="M0 360 C300 390 700 330 1220 372"/><path d="M0 380 C400 410 800 350 1220 392"/>
    </svg>
    <h2 class="abs h-section intro-title">Pools, Pool Enclosures and Hot Tubs from Kalmen Strand Pools</h2>
    <p class="abs intro-sub">Buy a pool and create an exclusive oasis in your garden</p>
    <div class="abs divider"></div>
    <p class="abs body-text intro-text">Invest in quality of life with a pool that provides relaxation, exercise and time with loved ones. Our sustainable and energy-efficient pools are built for the Nordic climate – with accessories such as heat pumps, lighting and purification systems, you get a complete and carefree pool experience.</p>
    <div class="btn btn-fade btn-sm" style="left:660px;top:280px;width:320px">Contact us today</div>
  </section>

  <section class="products">
    <h2 class="abs center-title serif" style="top:68px;font-size:40px">Our Products</h2>
    <svg class="arrow" style="left:74px" viewBox="0 0 36 36" fill="none" stroke="#2a86c9" stroke-width="2"><circle cx="18" cy="18" r="16"/><path d="M24 18H12m5-5l-5 5 5 5"/></svg>
    <div class="product" style="left:138px"><div class="thumb" role="img" aria-label="Photo of an outdoor pool"></div><span>Pool</span></div>
    <div class="product" style="left:334px"><div class="thumb" role="img" aria-label="Photo of thermo pool steps" style="background:linear-gradient(180deg,#b9bdc2,#6e7378)"></div><span>Thermo<br>Pool</span></div>
    <div class="product" style="left:530px"><div class="thumb" role="img" aria-label="Photo of a pool enclosure"></div><span>Pool<br>Enclosure</span></div>
    <div class="product" style="left:722px"><div class="thumb" role="img" aria-label="Photo of a pool deck" style="background:linear-gradient(180deg,#7ea36a,#c9b79a)"></div><span>Pool<br>Deck</span></div>
    <div class="product" style="left:918px"><div class="thumb" role="img" aria-label="Photo of a pool spa"></div><span>Pool<br>SPA</span></div>
    <svg class="arrow" style="left:1114px" viewBox="0 0 36 36" fill="none" stroke="#2a86c9" stroke-width="2"><circle cx="18" cy="18" r="16"/><path d="M12 18h12m-5-5l5 5-5 5"/></svg>
  </section>

  <section class="plan" role="img" aria-label="Water surface background">
    <h2 class="abs plan-title serif">Plan your dream pool with<br>Kalmen Strand Pools</h2>
    <p class="abs plan-text">Building a pool is an investment – we are with you all the way! From planning to finished pool, we make sure that you get a durable and stylish solution.</p>
    <ul class="abs checks">
      <li><svg width="22" height="22" viewBox="0 0 22 22" fill="none" stroke="#fff" stroke-width="2"><circle cx="11" cy="11" r="9"/><path d="M6.5 11l3 3 6-6"/></svg>Thermo pool, fiberglass – stainless steel pools</li>
      <li><svg width="22" height="22" viewBox="0 0 22 22" fill="none" stroke="#fff" stroke-width="2"><circle cx="11" cy="11" r="9"/><path d="M6.5 11l3 3 6-6"/></svg>Pool enclosures and hot tubs – extend the season</li>
      <li><svg width="22" height="22" viewBox="0 0 22 22" fill="none" stroke="#fff" stroke-width="2"><circle cx="11" cy="11" r="9"/><path d="M6.5 11l3 3 6-6"/></svg>Personal advice at every step</li>
    </ul>
    <div class="btn btn-sky btn-sm" style="left:450px;top:340px;width:320px">Contact us today</div>
  </section>

  <section class="create">
    <h2 class="abs center-title serif" style="top:56px;font-size:40px">Create your dream pool</h2>
    <p class="abs create-sub">Kalmen Strand Pools – Quality and Design in Perfect Harmony</p>
    <p class="abs create-text">Create your own oasis with an exclusive premium pool from Kalmen Strand. Our pools combine elegant design, sustainable construction and smart technology – tailored for the Nordic climate and your lifestyle.</p>
    <div class="tile" style="left:164px;top:216px;background:linear-gradient(160deg,#6a8f5c,#2b8ccc 55%,#1d6ea6)" role="img" aria-label="Photo of a composite fiberglass pool in a garden"><span>COMPOSITE FIBERGLASS POOLS</span></div>
    <div class="tile" style="left:624px;top:216px;background:linear-gradient(160deg,#4fa9de,#2a7fbd 60%,#1a5f92)" role="img" aria-label="Photo of a liner pool surface"><span>LINER POOLS</span></div>
    <div class="tile" style="left:164px;top:496px;background:linear-gradient(180deg,#c9a24e,#7ea35a 45%,#2f8fc9 75%,#3a4a55)" role="img" aria-label="Photo of a stainless steel pool with autumn trees"><span>STAINLESS STEEL POOLS</span></div>
    <div class="tile" style="left:624px;top:496px;background:linear-gradient(180deg,#7fb2d9,#3c4c5c 45%,#2a8ac4 75%,#2d3a46)" role="img" aria-label="Photo of a pool by a modern house"><span>NORDVIK POOLS</span></div>
    <div class="btn btn-sky btn-sm" style="left:450px;top:796px;width:320px">Explore all pools</div>
  </section>

  <section class="feature f-right" style="top:2868px">
    <div class="block block-left" role="img" aria-label="Water texture background"></div>
    <div class="frame" role="img" aria-label="Photo of grey thermo pool steps" style="background:linear-gradient(135deg,#8a7a62,#9ea2a6 40%,#6d7176)"></div>
    <div class="ftext">
      <h3 class="ftitle serif">Thermopool</h3>
      <p class="fsub">The optimal pool solution for durability and comfort</p>
      <p class="fbody">Thermopool – the perfect choice for those who want an energy-efficient, sustainable and comfortable pool. The robust construction with insulating blocks provides excellent heat retention and stability, adapted for the Nordic climate.</p>
      <div class="fbtns"><div class="btn btn-sky btn-sm" style="left:0;top:0;width:168px">Order now!</div><div class="btn btn-navy btn-sm" style="left:178px;top:0;width:168px">Get quotation</div></div>
    </div>
  </section>

  <section class="feature f-left" style="top:3376px">
    <div class="block block-right" role="img" aria-label="Water texture background"></div>
    <div class="frame" role="img" aria-label="Photo of a low pool enclosure on a wooden deck" style="background:linear-gradient(180deg,#3b4a3e,#50606b 45%,#b99a72 75%,#caa77c)"></div>
    <div class="ftext" style="top:136px">
      <h3 class="ftitle serif">Pool Enclosures</h3>
      <p class="fsub">Pool enclosures from Kalmen Strand Pools – an elegant, safe and energy-efficient solution</p>
      <p class="fbody">A pool enclosure from Kalmen Strand Pools is a smart investment in both style, safety and energy savings. Our exclusive premium enclosures protect your pool, extend the bathing season and elevate the entire feel of the garden – with maximum comfort and minimal energy loss.</p>
      <div class="fbtns"><div class="btn btn-sky btn-sm" style="left:0;top:0;width:168px">Order now!</div><div class="btn btn-navy btn-sm" style="left:178px;top:0;width:168px">Get quotation</div></div>
    </div>
  </section>

  <section class="feature f-right" style="top:3880px">
    <div class="block block-left" role="img" aria-label="Water texture background"></div>
    <div class="frame" role="img" aria-label="Photo of a pool deck in a walled garden" style="background:linear-gradient(160deg,#4f6a42,#8b9a86 45%,#c9c6bd)"></div>
    <div class="ftext" style="top:60px">
      <h3 class="ftitle serif">Pool Deck</h3>
      <p class="fsub">Create your dream garden with an exclusive pool deck from Kalmen Strand Pools</p>
      <p class="fbody">Create an exclusive and functional pool environment with a tailor-made pool deck from Kalmen Strand Pools. We combine design, comfort and sustainability – adapted to the Nordic climate.</p>
      <div class="mini-list"><b>Why choose our pool deck?</b>
        <span><svg width="14" height="14" viewBox="0 0 22 22" fill="none" stroke="#2a86c9" stroke-width="2.5"><circle cx="11" cy="11" r="9"/><path d="M6.5 11l3 3 6-6"/></svg>Stylish design that lifts your garden</span>
        <span><svg width="14" height="14" viewBox="0 0 22 22" fill="none" stroke="#2a86c9" stroke-width="2.5"><circle cx="11" cy="11" r="9"/><path d="M6.5 11l3 3 6-6"/></svg>Durable materials with minimal maintenance</span>
        <span><svg width="14" height="14" viewBox="0 0 22 22" fill="none" stroke="#2a86c9" stroke-width="2.5"><circle cx="11" cy="11" r="9"/><path d="M6.5 11l3 3 6-6"/></svg>Comfortable, safe and functional surface</span>
      </div>
      <div class="fbtns" style="margin-top:20px"><div class="btn btn-sky btn-sm" style="left:0;top:0;width:168px">Order now!</div><div class="btn btn-navy btn-sm" style="left:178px;top:0;width:168px">Get quotation</div></div>
    </div>
  </section>

  <section class="feature f-left" style="top:4384px">
    <div class="block block-right" role="img" aria-label="Water texture background"></div>
    <div class="frame" role="img" aria-label="Photo of an outdoor spa with mountain view" style="background:linear-gradient(180deg,#8fb6d6,#5f7a52 40%,#3aa0d6 70%,#c9ccd0)"></div>
    <div class="ftext" style="top:136px">
      <h3 class="ftitle serif">Premium SPA</h3>
      <p class="fsub">Experience total relaxation with our premium spas</p>
      <p class="fbody">Create your own luxurious spa oasis with a premium spa from Kalmen Strand Pools. Our hot tubs are designed to provide maximum comfort, durability and energy efficiency, so you can enjoy warm, relaxing baths all year round.</p>
      <div class="fbtns"><div class="btn btn-sky btn-sm" style="left:0;top:0;width:168px">Order now!</div><div class="btn btn-navy btn-sm" style="left:178px;top:0;width:168px">Get quotation</div></div>
    </div>
  </section>

  <section class="feature f-right" style="top:4888px">
    <div class="block block-left" role="img" aria-label="Water texture background"></div>
    <div class="frame" role="img" aria-label="Photo of two pool cleaning robots by a pool" style="background:linear-gradient(180deg,#c9d3dc,#6f8e6c 40%,#3aa6dc 60%,#7fcbe8)"></div>
    <div class="ftext" style="top:48px">
      <h3 class="ftitle serif">Aquaron Pool<br>Robot</h3>
      <p class="fsub">Premium pool robots – the smart solution for a crystal clear pool.</p>
      <p class="fbody">Keeping your pool clean and well-maintained has never been easier! Discover our premium pool robots – the ultimate solution for efficient and automated pool cleaning. With advanced technology and high performance, our pool robots ensure that your pool is free of dirt, leaves and particles – whether they are on the bottom, walls or waterline.</p>
      <div class="fbtns"><div class="btn btn-sky btn-sm" style="left:0;top:0;width:168px">Buy now!</div></div>
    </div>
  </section>

  <section class="summer" role="img" aria-label="Photo of a woman in a sun hat sitting at the edge of a pool, seen from behind">
    <h2 class="abs summer-title serif">SUMMER 2026<br>Pool Dreams</h2>
    <p class="abs summer-text">Make your dream come true this summer. Book a consultation now and get your pool ready in time for the warm season, with expert help from planning to the first swim.</p>
    <div class="btn btn-navy" style="left:88px;top:412px;width:320px">Read more here!</div>
  </section>

  <section class="reviews">
    <h2 class="abs h-section" style="left:88px;top:92px">See Why Homeowners<br>Love Our Pools</h2>
    <div class="abs rating">
      <span style="font-weight:500;color:#4a5a6a">Ratewell</span>
      <span>Excellent</span>
      <span class="stars">★★★★★</span>
      <span style="color:#f5b922">4.9</span>
      <span>50 Reviews</span>
      <div class="btn btn-fade btn-sm" style="left:770px;top:16px;width:250px">Write a review</div>
    </div>
    <div class="card" style="left:88px"><span class="g-mark"></span><h4>Ingrid Falk</h4><div class="stars">★★★★★</div><p>Many thanks to the team for professional and nice treatment. We received a quick response throughout the purchasing process. Very good quality of products, they really know the pool. Highly recommended!</p></div>
    <div class="card" style="left:442px"><span class="g-mark"></span><h4>Johan Berglind</h4><div class="stars">★★★★★</div><p>This company set absolutely standards in quality, fast supply and service. The staff and especially the owner who really knows what he is talking about. I have bought a pool that has now been standing and working for years without any problems. Not even the pool cloth has been replaced in these years. It's time for us now to assemble a deeper pool and I sincerely hope to get help from these professionals on pools and peripherals. So this company and the staff are definitely worth it. I recommend them immediately.</p></div>
    <div class="card" style="left:796px"><span class="g-mark"></span><h4>Nils Ekdahl</h4><div class="stars">★★★★★</div><p>Exceptional service from start to finish. When my old pool broke down they were quickly out and after a few months I have a new premium pool and a new pool cover. The work and contact with the seller went smoothly and with quick responses. Can highly recommend to anyone who is looking for the highest quality at a reasonable price.</p></div>
  </section>

  <footer class="footer">
    <div class="abs f-brand">Kalmen Strand</div>
    <div class="abs f-contact">
      <div>☎ +46 480 00 00 00</div>
      <div>✉ info@kalmenstrand.se</div>
      <div>⌖ Strandvägen 4, 392 30 Kalmar, Sweden</div>
    </div>
    <div class="abs socials"><i></i><i></i><i></i><i></i><i></i></div>
    <div class="fcol" style="left:504px"><h5>PRODUCTS</h5><div>Pools</div><div>Pool enclosure</div><div>Hot tub</div><div>Accessories</div><div>Building a pool Kalmar</div><div>Building a pool in Småland</div><div>Building a pool Stockholm</div><div>Building a pool Skåne</div><div>Building a pool Gothenburg</div><div>Building a pool in the rest of Sweden</div></div>
    <div class="fcol" style="left:816px"><h5>CUSTOMER SERVICE</h5><div>Payments</div><div>Shipping and delivery</div><div>Returns</div><div>Support</div><div>Terms and conditions</div></div>
    <div class="fcol" style="left:1048px"><h5>CONTACT US</h5><div>About us</div><div>Service</div><div>Blog</div><div>Contact</div></div>
    <div class="bottom-bar">2026© All right reserved by Kalmen Strand</div>
  </footer>

</div>
</body>
</html>
```